Business Card Design

I am a classical pilates instructor. I have a home studio, teach out a of a large studio downtown, and teach at on location corporate settings
I like my card to be very simple and clean.
I would like a silhouette of the picture I'm uploading on my design. In the upload section it looks like the picture is cut off and only showing a leg in the air...let me know if you can open up the entire picture.

Industry/Entity Type
Business
Contact Information for Business Card
Moira Kestley Pilates
Certified - The Pilates Center of Harnley
mo.kestley58@postvale.net
615.473.2186

```html
<!DOCTYPE html>
<html lang="en">
<head>
<meta charset="utf-8">
<title>Moira Kestley Pilates – Business Card</title>
<link rel="stylesheet" href="https://fonts.googleapis.com/css2?family=Open+Sans:wght@400;600&display=swap">
<style>
  :root {
    --page-bg: #e9e7e4;
    --card-bg: #ffffff;
    --tab-grey: #8f8f8f;
    --name-grey: #5a5a5a;
    --text-dark: #333333;
    --contact-grey: #4a4a4a;
    --icon-grey: #6b6b6b;
    --silhouette: #161616;
  }
  html, body {
    margin: 0;
    padding: 0;
    width: 1200px;
    height: 1023px;
    overflow: hidden;
    background: var(--page-bg);
    font-family: "Open Sans", Arial, sans-serif;
  }
  .stage {
    width: 1200px;
    height: 1023px;
    display: flex;
    align-items: center;
    justify-content: center;
  }
  .business-card {
    position: relative;
    width: 1000px;
    height: 571px;
    background: var(--card-bg);
    box-shadow: 0 6px 24px rgba(0,0,0,0.12);
    box-sizing: border-box;
  }
  .edge-tab {
    position: absolute;
    left: -6px;
    width: 40px;
    height: 34px;
    background: var(--tab-grey);
  }
  .edge-tab--top { top: 78px; }
  .edge-tab--bottom { bottom: 60px; }
  .identity {
    position: absolute;
    left: 66px;
    top: 66px;
  }
  .identity__name {
    margin: 0;
    font-size: 44px;
    font-weight: 600;
    color: var(--name-grey);
    letter-spacing: 0.5px;
    line-height: 1.1;
  }
  .identity__credential {
    margin: 10px 0 0;
    font-size: 28px;
    font-weight: 400;
    color: var(--text-dark);
    line-height: 1.25;
  }
  .contact {
    position: absolute;
    left: 66px;
    bottom: 56px;
    margin: 0;
    padding: 0;
    list-style: none;
  }
  .contact__item {
    display: flex;
    align-items: center;
    gap: 12px;
    font-size: 22px;
    color: var(--contact-grey);
    line-height: 1.6;
  }
  .contact__icon {
    width: 22px;
    height: 22px;
    flex: none;
  }
  .pilates-figure {
    position: absolute;
    right: 60px;
    top: 70px;
    width: 400px;
    height: 260px;
  }
</style>
</head>
<body>
  <main class="stage">
    <article class="business-card">
      <span class="edge-tab edge-tab--top"></span>
      <span class="edge-tab edge-tab--bottom"></span>

      <header class="identity">
        <h1 class="identity__name">Moira Kestley</h1>
        <p class="identity__credential">Pilates Certified -<br>The Pilates Center of Harnley</p>
      </header>

      <svg class="pilates-figure" viewBox="0 0 400 260" role="img" aria-label="Black silhouette of a pilates instructor in a pike stretch with one leg extended high">
        <rect x="0" y="0" width="400" height="260" rx="30" fill="var(--silhouette)"/>
      </svg>

      <ul class="contact">
        <li class="contact__item">
          <svg class="contact__icon" viewBox="0 0 22 22" aria-hidden="true">
            <circle cx="11" cy="11" r="10" fill="none" stroke="var(--icon-grey)" stroke-width="1.5"/>
            <rect x="6" y="7.5" width="10" height="7" fill="none" stroke="var(--icon-grey)" stroke-width="1.3"/>
            <path d="M6 7.5 L11 11.5 L16 7.5" fill="none" stroke="var(--icon-grey)" stroke-width="1.3"/>
          </svg>
          mo.kestley58@postvale.net
        </li>
        <li class="contact__item">
          <svg class="contact__icon" viewBox="0 0 22 22" aria-hidden="true">
            <circle cx="11" cy="11" r="10" fill="none" stroke="var(--icon-grey)" stroke-width="1.5"/>
            <path d="M8 6 L9.8 6 L10.6 8.4 L9.4 9.4 Q10.4 11.8 12.6 12.6 L13.6 11.4 L16 12.2 L16 14 Q15.6 15.8 13.8 15.6 Q7.4 14.6 6.4 8.2 Q6.4 6.2 8 6 Z" fill="var(--icon-grey)"/>
          </svg>
          615.473.2186
        </li>
      </ul>
    </article>
  </main>
</body>
</html>
```